Business Card for Language School (2 locations)

We need a sleek business card for a language school that is looking to update our image to be more professional. We work with students ages Pre-Kindergarten through adults. Our idea is to have an all-black business card with white or silver lettering. On the front will be the name of our school (Bright Maple English Academy), and on the back there will be information for our location, phone number, email, and website (and possibly social media information). We have two school branches, so the address, phone number, and email address will be different for each branch, but all of the other information will stay the same. We'd like each branch to have a different color card edge that is neon. We are also open to suggestions and new ideas!

Some answers to questions we have received:
1. The reason we haven't added a logo is because we are looking to get a new one. We hadn't originally planned to do that at this time, but we are going to look into updating our project to include that as another aspect of it. We had previously planned to just include the school name on the front without a logo at this time.
2. We currently have two branches of our school, and we want our business card design to be uniform for each location. While it might make sense to put the information on one card right now, we plan to have more locations in the future, so we want to plan ahead with a unified design right now.
3. Our school addresses and phone numbers can be found on our website: www.brightmapleenglish.example (at the bottom of the page)!
Updates

Part of this contest is also a new logo design. Our previous design was a train, which we would be open to keeping if it had an updated, sleeker design.

Contact Information for Business Card

Card #1:
Bright Maple English Academy (Qiaolin Branch)
Yuqing W. Rd. Sec. 3, Lane 412, No. 29, 1F
Beitou District, Taipei City 11268
02-2649-3058
qiaolin@brightmapleenglish.example

Card #2:
Bright Maple English Academy (Fenghe Branch)
Fulan Road, No. 318, 1F
Songshan District, Taipei City 10573
02-2761-4402
fenghe@brightmapleenglish.example

Both cards:
Website: www.brightmapleenglish.example
Facebook: www.facebook.com/brightmapleenglish
Instagram: @brightmapleenglish

```html
<!DOCTYPE html>
<html lang="en">
<head>
<meta charset="utf-8">
<title>Bright Maple English Academy — Business Card</title>
<link rel="stylesheet" href="https://fonts.googleapis.com/css2?family=Saira+Condensed:wght@400;500&display=swap">
<style>
  :root {
    --page: #ecebe8;
    --card-black: #1b1b1c;
    --card-black-deep: #111112;
    --band: #0d0d0e;
    --ink: #ffffff;
    --accent: #e0141b;
    --shadow: rgba(0, 0, 0, 0.28);
  }
  * { box-sizing: border-box; margin: 0; padding: 0; }
  html, body {
    width: 1200px;
    height: 942px;
    overflow: hidden;
    background: var(--page);
    font-family: "Saira Condensed", "Arial Narrow", sans-serif;
    color: var(--ink);
  }
  .canvas { position: relative; width: 1200px; height: 942px; }

  .card {
    position: absolute;
    width: 640px;
    height: 410px;
    background: linear-gradient(160deg, var(--card-black) 0%, var(--card-black-deep) 100%);
    box-shadow: 0 10px 26px var(--shadow);
    overflow: hidden;
  }
  .card--front { left: 90px; top: 50px; }
  .card--back  { left: 470px; top: 482px; }

  /* Front */
  .edge-band {
    position: absolute;
    left: 0; right: 0;
    height: 46px;
    background: var(--band);
  }
  .edge-band--top { top: 0; }
  .edge-band--bottom { bottom: 0; }
  .edge-band::after {
    content: "";
    position: absolute;
    left: 0; right: 0;
    height: 3px;
    background: linear-gradient(90deg, #3a3a3a 0%, var(--ink) 30%, var(--accent) 70%, #3a3a3a 100%);
  }
  .edge-band--top::after { bottom: 0; }
  .edge-band--bottom::after { top: 0; }

  .wordmark {
    position: absolute;
    left: 0; right: 0;
    top: 46px; bottom: 46px;
    display: flex;
    align-items: center;
    justify-content: center;
    gap: 22px;
  }
  .wordmark__mark {
    width: 22px; height: 22px;
    background: var(--accent);
  }
  .wordmark__name {
    font-size: 46px;
    font-weight: 500;
    line-height: 1.05;
    color: var(--ink);
  }

  /* Back */
  .back-art { position: absolute; inset: 0; }
  .school {
    position: absolute;
    right: 26px;
    top: 22px;
    text-align: right;
    line-height: 1.3;
  }
  .school__name { font-size: 27px; font-weight: 500; color: var(--ink); }
  .school__branch { font-size: 25px; color: var(--accent); }

  .contact-list {
    position: absolute;
    left: 26px;
    top: 126px;
    list-style: none;
    font-size: 19px;
    line-height: 1.5;
  }
  .contact-list li { display: flex; align-items: flex-start; gap: 12px; margin-bottom: 10px; }
  .contact-list li:nth-child(2) { margin-bottom: 12px; }
  .icon { flex: 0 0 22px; width: 22px; height: 22px; margin-top: 4px; }

  .social-list {
    position: absolute;
    left: 414px;
    top: 260px;
    list-style: none;
    font-size: 20px;
    line-height: 1.45;
  }
  .social-list li { display: flex; align-items: flex-start; gap: 12px; margin-bottom: 14px; }
  .social-dot {
    flex: 0 0 20px;
    width: 20px; height: 20px;
    margin-top: 5px;
    border-radius: 50%;
    background: var(--ink);
  }
</style>
</head>
<body>
<main class="canvas">

  <section class="card card--front" aria-label="Business card front">
    <div class="edge-band edge-band--top"></div>
    <div class="wordmark">
      <span class="wordmark__mark" aria-hidden="true"></span>
      <h1 class="wordmark__name">Bright Maple<br>English Academy</h1>
    </div>
    <div class="edge-band edge-band--bottom"></div>
  </section>

  <section class="card card--back" aria-label="Business card back">
    <svg class="back-art" viewBox="0 0 640 410" aria-hidden="true">
      <defs>
        <linearGradient id="divider-glow" x1="0" y1="0" x2="0" y2="1">
          <stop offset="0" stop-color="#e0141b"/>
          <stop offset="0.5" stop-color="#ffffff"/>
          <stop offset="1" stop-color="#ffffff"/>
        </linearGradient>
      </defs>
      <polygon points="0,0 292,0 382,410 0,410" fill="#161617"/>
      <line x1="292" y1="0" x2="382" y2="410" stroke="#e0141b" stroke-width="7" opacity="0.35"/>
      <line x1="292" y1="0" x2="382" y2="410" stroke="url(#divider-glow)" stroke-width="2.5"/>
    </svg>

    <header class="school">
      <p class="school__name">Bright Maple English Academy</p>
      <p class="school__branch">(Qiaolin Branch)</p>
    </header>

    <ul class="contact-list">
      <li>
        <svg class="icon" viewBox="0 0 22 22" aria-label="Phone"><circle cx="11" cy="11" r="11" fill="#fff"/><path d="M7.5 6c.6-.5 1.3-.4 1.6.2l.9 1.7c.2.5.1 1-.3 1.3l-.6.5c.5 1.2 1.5 2.2 2.7 2.7l.5-.6c.3-.4.9-.5 1.3-.3l1.7.9c.6.3.7 1 .2 1.6l-.8.9c-.6.6-1.6.7-2.4.3-2.4-1.1-4.100-2.800-5.200-5.200-.4-.8-.2-1.8.4-2.4z" fill="#e0141b"/></svg>
        <span>02-2649-3058</span>
      </li>
      <li>
        <svg class="icon" viewBox="0 0 22 22" aria-label="Address"><circle cx="11" cy="11" r="11" fill="#fff"/><path d="M11 4.5a4.3 4.3 0 0 0-4.3 4.3c0 3.2 4.3 8.4 4.3 8.4s4.3-5.2 4.3-8.4A4.3 4.3 0 0 0 11 4.5zm0 6a1.7 1.7 0 1 1 0-3.4 1.7 1.7 0 0 1 0 3.4z" fill="#e0141b"/></svg>
        <span>Yuqing W. Rd. Sec. 3,<br>Lane 412, No. 29, 1F<br>Beitou District, Taipei City 11268</span>
      </li>
      <li>
        <svg class="icon" viewBox="0 0 22 22" aria-label="Email"><circle cx="11" cy="11" r="11" fill="#fff"/><rect x="5.5" y="7" width="11" height="8" rx="1" fill="#e0141b"/><path d="M5.8 7.4 11 11.4l5.2-4" fill="none" stroke="#fff" stroke-width="1.2"/></svg>
        <span>qiaolin@brightmapleenglish.example</span>
      </li>
      <li>
        <svg class="icon" viewBox="0 0 22 22" aria-label="Website"><circle cx="11" cy="11" r="11" fill="#fff"/><g fill="none" stroke="#e0141b" stroke-width="1.3"><circle cx="11" cy="11" r="5.5"/><ellipse cx="11" cy="11" rx="2.3" ry="5.5"/><path d="M5.5 11h11"/></g></svg>
        <span>www.brightmapleenglish.example</span>
      </li>
    </ul>

    <ul class="social-list">
      <li><span class="social-dot" aria-hidden="true"></span><span>www.friendspace.example/<br>brightmapleenglish</span></li>
      <li><span class="social-dot" aria-hidden="true"></span><span>@brightmapleenglish</span></li>
    </ul>
  </section>

</main>
</body>
</html>
```